New web design for a service provider in the medical field

We are looking for a new design for our website. We are a company that repairs and sells medical endoscopes. Our customers include doctors and hospitals. Our current website can be found at https://lumenfix.example/en/lumenfix-english.
We need a new web design (without programming) for the following 3 pages:
-Startpage https://lumenfix.example/en/lumenfix-english/
-Used endoscopes https://lumenfix.example/en/used-endoscopes/
-Purchase https://lumenfix.example/en/purchase/
The design should be modern and stylish.
The blue color of the logo should be reflected on the page, but not too intrusive.
I have uploaded the images from the header. If more images are needed, let me know and I will upload them.

Target Market(s)
Doctors and hospitals

```html
<!DOCTYPE html>
<html lang="en">
<head>
<meta charset="utf-8">
<title>LumenFix – Endoscope Repair</title>
<link rel="stylesheet" href="https://fonts.googleapis.com/css2?family=Nunito:wght@300;400;500;600;700;800;900&display=swap">
<style>
:root{
  --navy:#0b3a5e;
  --blue:#29a8e0;
  --ink:#111418;
  --text:#2a2f36;
  --line:#e6ebf0;
  --pale:#eaf5fc;
  --footer:#04192b;
  --footer-line:#1a3149;
}
*{margin:0;padding:0;box-sizing:border-box}
html,body{width:1200px;height:3332px;overflow:hidden}
body{font-family:'Nunito',sans-serif;color:var(--text);background:#fff;position:relative}
a{color:inherit;text-decoration:none}
.wrap{width:900px;margin:0 auto;position:relative}
.btn{display:inline-block;background:var(--navy);color:#fff;border-radius:30px;font-weight:500;font-size:14px;text-align:center}

/* top bar */
.topbar{height:90px;border-bottom:1px solid var(--line);position:relative}
.brand{position:absolute;left:154px;top:24px;display:flex;align-items:center;gap:8px}
.brand .dot{width:14px;height:14px;border-radius:50%;background:var(--blue)}
.brand .name{font-weight:800;font-size:19px;color:var(--navy);letter-spacing:.2px}
.contact-top{position:absolute;left:562px;top:38px;display:flex;gap:22px;font-size:13px;color:var(--ink);align-items:center}
.contact-top span{display:flex;align-items:center;gap:10px}
.vdiv{position:absolute;left:936px;top:0;width:1px;height:90px;background:var(--line)}
.social-top{position:absolute;left:994px;top:39px;display:flex;gap:13px}
.sq{width:18px;height:18px;border-radius:4px;background:var(--navy)}

/* nav */
.nav{height:53px;border-bottom:1px solid var(--line);position:relative}
.nav ul{list-style:none;position:absolute;left:157px;top:19px;display:flex;gap:21px;font-size:12px;color:var(--ink)}
.nav li.active{color:var(--blue)}
.burger{position:absolute;left:1026px;top:19px;width:19px}
.burger i{display:block;height:2px;background:var(--navy);margin-bottom:5px}

/* hero */
.hero{height:475px;position:relative;overflow:hidden}
.hero-photo{position:absolute;inset:0;background:linear-gradient(100deg,#ffffff 0%,#f7f8f9 35%,#d8dbde 62%,#9da3a8 78%,#e4e6e8 100%)}
.hero-copy{position:absolute;left:149px;top:70px}
.hero h1{font-weight:300;font-size:70px;line-height:73px;color:var(--ink)}
.hero h1 strong{font-weight:900;color:var(--blue);display:block}
.hero .btn{margin-top:38px;width:305px;height:54px;line-height:54px;font-size:15px;font-weight:600}

/* service cards */
.services{height:459px;position:relative}
.card{position:absolute;top:74px;width:282px;height:337px;border:1px solid var(--line);border-radius:4px;text-align:center;box-shadow:0 6px 18px rgba(41,168,224,.08);padding:40px 14px 0}
.card svg{height:46px}
.card h3{font-weight:500;font-size:22px;color:var(--ink);margin:14px 0 16px}
.card p{font-size:11.5px;line-height:19px;color:var(--text)}
.card .btn{position:absolute;left:66px;top:262px;width:148px;height:40px;line-height:40px}

/* about */
.about{height:490px;position:relative}
.ph{position:absolute;background:linear-gradient(135deg,#e8eaec,#9fa5ab);box-shadow:0 4px 14px rgba(0,0,0,.12)}
.about-copy{position:absolute;left:633px;top:45px;width:410px}
.about h2{font-weight:500;font-size:30px;line-height:36px;color:var(--ink)}
.about h2 em{display:block;font-style:normal;font-weight:400;color:var(--blue);margin-top:4px}
.about p{font-size:11.5px;line-height:20px;margin-top:18px}
.about p+p{margin-top:10px}

/* faulty band */
.faulty{height:424px;position:relative;overflow:hidden;background:linear-gradient(90deg,#f4f5f6 0%,#fbfbfb 40%,#f1f2f3 100%)}
.faulty-photo{position:absolute;left:520px;top:40px;width:680px;height:340px;background:radial-gradient(ellipse at 45% 55%,#5a6068 0%,#a4a9ae 35%,rgba(240,241,242,0) 70%)}
.faulty-copy{position:absolute;left:153px;top:108px}
.faulty h2{font-weight:900;font-size:46px;line-height:54px;color:var(--ink)}
.faulty h2 span{color:var(--blue);display:block}
.faulty .lead{font-size:15px;margin-top:8px;color:var(--ink)}
.faulty .simple{font-size:26px;margin-top:14px;color:var(--ink)}
.faulty .btn{margin-top:32px;width:147px;height:40px;line-height:40px}

/* features */
.features{height:738px;background:linear-gradient(180deg,var(--pale),#fff 80%);position:relative;text-align:center}
.features h2{padding-top:52px;font-weight:500;font-size:31px;line-height:42px;color:var(--ink)}
.feat{position:absolute;width:270px;text-align:center}
.feat svg{height:46px}
.feat h3{font-weight:500;font-size:23px;line-height:28px;color:var(--ink);margin:8px 0 12px}
.feat p{font-size:11.5px;line-height:19px}
.features .btn{position:absolute;left:447px;top:620px;width:305px;height:54px;line-height:54px;font-size:15px;font-weight:600}

/* footer */
.footer{height:606px;background:var(--footer);color:#c9d3dd;position:relative}
.footer .brand{left:158px;top:80px}
.footer .brand .name{color:#fff;font-size:21px}
.footer .help{position:absolute;right:155px;top:66px;font-weight:800;font-size:38px;color:#fff}
.footer .send{position:absolute;left:839px;top:135px;width:206px;height:54px;line-height:54px;background:var(--blue);color:#fff;border-radius:30px;font-weight:600;font-size:15px;text-align:center}
.hr{position:absolute;left:153px;width:892px;height:1px;background:var(--footer-line)}
.fcol{position:absolute;top:280px}
.fcol h4{font-weight:400;font-size:24px;color:#fff;margin-bottom:24px}
.fcol li{list-style:none;font-size:12px;margin-bottom:14px;display:flex;align-items:center;gap:14px}
.fcol.links li{font-size:12px;margin-bottom:12px}
.social-foot{position:absolute;left:671px;top:336px;display:flex;gap:12px}
.social-foot .sq{background:var(--blue)}
.copy{position:absolute;left:0;right:0;top:571px;text-align:center;font-size:12px}
</style>
</head>
<body>

<header class="topbar">
  <div class="brand"><span class="dot"></span><span class="name">LumenFix</span></div>
  <div class="contact-top">
    <span><svg width="14" height="14" viewBox="0 0 24 24"><path fill="#29a8e0" d="M6.6 10.8a15 15 0 006.6 6.6l2.2-2.2c.3-.3.7-.4 1-.2 1.1.4 2.3.6 3.6.6.6 0 1 .4 1 1V20c0 .6-.4 1-1 1A17 17 0 013 4c0-.6.4-1 1-1h3.5c.6 0 1 .4 1 1 0 1.3.2 2.5.6 3.6.1.3 0 .7-.2 1z"/></svg>+49 4100 555 010-0</span>
    <span><svg width="16" height="12" viewBox="0 0 16 12"><rect width="16" height="12" rx="1.5" fill="#29a8e0"/><path d="M1 1l7 5 7-5" stroke="#fff" stroke-width="1.4" fill="none"/></svg>info@lumenfix.example</span>
  </div>
  <div class="vdiv"></div>
  <div class="social-top"><span class="sq"></span><span class="sq"></span></div>
</header>

<nav class="nav">
  <ul>
    <li class="active">HOME</li><li>ENDOSCOPE REPAIR</li><li>USED ENDOSCOPES</li><li>ENDOSCOPY SYSTEMS</li><li>ENDOSCOPY ACCESSORIES</li><li>PURCHASE</li>
  </ul>
  <div class="burger"><i></i><i></i><i></i></div>
</nav>

<section class="hero">
  <div class="hero-photo" role="img" aria-label="Close-up photo of an endoscope control body with angulation knobs on a white stand"></div>
  <div class="hero-copy">
    <h1>Put Your<strong>Endoscope In</strong>Reliable Hands!</h1>
    <a class="btn" href="#">Learn More About LumenFix!</a>
  </div>
</section>

<section class="services">
  <div class="card" style="left:154px">
    <svg viewBox="0 0 46 46"><circle cx="20" cy="24" r="13" fill="#29a8e0"/><circle cx="20" cy="24" r="5" fill="#fff"/><rect x="30" y="6" width="6" height="34" rx="3" fill="#0b3a5e"/></svg>
    <h3>Repair Service</h3>
    <p>Manufacturer-independent we repair and maintain endoscopes, individual components (e.g. processors or light sources), accessories and peripherals of the manufacturers Orvane, Penrix and Fujora.</p>
    <a class="btn" href="#">Repair Request</a>
  </div>
  <div class="card" style="left:459px">
    <svg viewBox="0 0 46 46"><path d="M8 26L26 8h14v14L22 40z" fill="#29a8e0"/><circle cx="34" cy="14" r="3" fill="#fff"/></svg>
    <h3>Sale Endoscopes</h3>
    <p>Our regular stock includes refurbished gastroscopes, coloscopes, bronchoscopes, cystoscopes and duodenoscopes from the well-known manufacturers Orvane, Penrix and Fujora.</p>
    <a class="btn" href="#">Purchase Request</a>
  </div>
  <div class="card" style="left:764px">
    <svg viewBox="0 0 46 46"><rect x="6" y="22" width="34" height="18" rx="2" fill="#29a8e0"/><rect x="6" y="28" width="34" height="3" fill="#0b3a5e"/><circle cx="23" cy="12" r="8" fill="#0b3a5e"/><path d="M19 12l3 3 5-6" stroke="#fff" stroke-width="2" fill="none"/></svg>
    <h3>Purchase Endoscopes</h3>
    <p>We are very interested in buying your old endoscopes – even defective and dismantled! We offer fair conditions! Please contact us for a purchase offer!</p>
    <a class="btn" href="#">Sell Device</a>
  </div>
</section>

<section class="about">
  <div class="ph" style="left:214px;top:88px;width:160px;height:227px" role="img" aria-label="Photo of endoscope control knobs"></div>
  <div class="ph" style="left:422px;top:58px;width:154px;height:145px;background:linear-gradient(135deg,#dfe9f1,#8ea3b5)" role="img" aria-label="Photo of a doctor examining a patient"></div>
  <div class="ph" style="left:339px;top:228px;width:160px;height:150px;background:linear-gradient(135deg,#f3f4f5,#7c8288)" role="img" aria-label="Photo of two endoscopes lying on a white surface"></div>
  <div class="about-copy">
    <h2>Endoscope Repairs And Second Hand Endoscopes From LumenFix<em>Cause The Outcome Matters!</em></h2>
    <p>LumenFix is a privileged partner for the start-up facility or optimisation of existing healthcare facilities, doctor's offices and hospitals. The quality and reliability of our products and our offered service are our best advertisement!</p>
    <p>As a result of optimised processes and highly qualified specialists in our company, we can work very quickly and with high quality for your benefit of least possible restrictions in your doctor's office or in your hospital.</p>
  </div>
</section>

<section class="faulty">
  <div class="faulty-photo" role="img" aria-label="Photo of a video endoscope with its connector and insertion tube"></div>
  <div class="faulty-copy">
    <h2><span>Faulty</span>Endoscope?</h2>
    <p class="lead">We ensure quick and smooth repairs!</p>
    <p class="simple">Simple Place a</p>
    <a class="btn" href="#">Pick-Up Order</a>
  </div>
</section>

<section class="features">
  <h2>LumenFix GmbH, Your Decision<br>For Your Future</h2>
  <div class="feat" style="left:160px;top:180px">
    <svg viewBox="0 0 46 46"><circle cx="26" cy="24" r="14" fill="#29a8e0"/><circle cx="26" cy="24" r="6" fill="#fff"/><rect x="4" y="16" width="10" height="3" fill="#0b3a5e"/><rect x="2" y="23" width="10" height="3" fill="#0b3a5e"/><rect x="4" y="30" width="10" height="3" fill="#0b3a5e"/></svg>
    <h3>Fast Repairs</h3>
    <p>Keep potential disruptions in your doctor's office or in your hospital at minimum as a result of optimized processes and highly qualified specialists in our company</p>
  </div>
  <div class="feat" style="left:465px;top:180px">
    <svg viewBox="0 0 46 46"><rect x="10" y="28" width="6" height="14" fill="#29a8e0"/><rect x="19" y="20" width="6" height="22" fill="#29a8e0"/><rect x="28" y="12" width="6" height="30" fill="#29a8e0"/><rect x="37" y="4" width="6" height="38" fill="#0b3a5e"/><circle cx="8" cy="10" r="6" fill="#0b3a5e"/></svg>
    <h3>Highly Cost Efficient</h3>
    <p>Benefit from our first class recommendations and implementation by our experienced staff. Our goals is to find the best solutions together with you at the best lowest price point.</p>
  </div>
  <div class="feat" style="left:770px;top:180px">
    <svg viewBox="0 0 46 46"><rect x="8" y="24" width="30" height="16" rx="2" fill="#29a8e0"/><rect x="14" y="12" width="10" height="12" fill="#0b3a5e"/><circle cx="32" cy="10" r="5" fill="#29a8e0"/></svg>
    <h3>On-Site Service</h3>
    <p>We will gladly pay you a visit to to carry out analysis and repairs on site. Due to our many years of experience – it doesn't get any faster (whigleithin a 250 km range)</p>
  </div>
  <div class="feat" style="left:160px;top:382px">
    <svg viewBox="0 0 46 46"><rect x="4" y="20" width="9" height="22" rx="2" fill="#29a8e0"/><path d="M15 22l8-16c3 0 5 2 4 6l-2 6h12c3 0 4 3 3 5l-4 14c-1 3-3 5-6 5H15z" fill="#29a8e0"/></svg>
    <h3>Loan Equipment Service</h3>
    <p>Use our service of high-quality loan devices during the downtime of your defective endoscope (limited to stock)</p>
  </div>
  <div class="feat" style="left:465px;top:382px">
    <svg viewBox="0 0 46 46"><rect x="8" y="6" width="26" height="36" rx="2" fill="none" stroke="#29a8e0" stroke-width="3"/><rect x="14" y="14" width="14" height="3" fill="#0b3a5e"/><rect x="14" y="22" width="14" height="3" fill="#0b3a5e"/><path d="M30 40l10-18" stroke="#29a8e0" stroke-width="4"/></svg>
    <h3>Without a Maintenance Contract</h3>
    <p>Benefit from our first class recommendations and implementation by our experienced staff. Our goals is to find the best solutions together with you at the best lowest price point.</p>
  </div>
  <div class="feat" style="left:770px;top:382px">
    <svg viewBox="0 0 46 46"><circle cx="23" cy="18" r="14" fill="none" stroke="#29a8e0" stroke-width="3"/><circle cx="23" cy="18" r="9" fill="#29a8e0"/><path d="M14 30l-5 12 7-3 4 5 3-10M32 30l5 12-7-3-4 5-3-10" fill="#29a8e0"/></svg>
    <h3>First Class Service</h3>
    <p>Our clients always come first!</p>
  </div>
  <a class="btn" href="#">Learn More About LumenFix!</a>
</section>

<footer class="footer">
  <div class="brand"><span class="dot"></span><span class="name">LumenFix</span></div>
  <h2 class="help">How Can We Help You?</h2>
  <a class="send" href="#">Send Us A Message</a>
  <div class="hr" style="top:229px"></div>
  <div class="fcol" style="left:153px">
    <h4>Contact Us</h4>
    <ul>
      <li><svg width="14" height="14" viewBox="0 0 24 24"><path fill="#29a8e0" d="M6.6 10.8a15 15 0 006.6 6.6l2.2-2.2c.3-.3.7-.4 1-.2 1.1.4 2.3.6 3.6.6.6 0 1 .4 1 1V20c0 .6-.4 1-1 1A17 17 0 013 4c0-.6.4-1 1-1h3.5c.6 0 1 .4 1 1 0 1.3.2 2.5.6 3.6.1.3 0 .7-.2 1z"/></svg>+49 4100 555 010-0</li>
      <li><svg width="16" height="12" viewBox="0 0 16 12"><rect width="16" height="12" rx="1.5" fill="#29a8e0"/><path d="M1 1l7 5 7-5" stroke="#04192b" stroke-width="1.4" fill="none"/></svg>info@lumenfix.example</li>
    </ul>
  </div>
  <div class="fcol links" style="left:427px">
    <h4>Quick Link</h4>
    <ul><li>Informations</li><li>About Us</li><li>Contact Us</li><li>TOS</li><li>Copyrights</li><li>Privacy Policy</li></ul>
  </div>
  <div class="social-foot"><span class="sq"></span><span class="sq"></span></div>
  <div class="hr" style="top:545px"></div>
  <p class="copy">© 2022 LumenFix GmbH</p>
</footer>

</body>
</html>
```